KWI Business Card

Please create a creative design for a business card using the new theme from the Logo & website. This company's main focus is food manufacturing building construction. Please integrate the new logo attached.

Please use the following information for the demo card:

Korvel Walls, Inc.
Dana Whitcombe
dwhitcombe@korvelwalls.example
Cell: 312-555-0178
218 Larkmoor Ave
Brenwick, OH 60418

See pictures and more information on the website.

www.korvelwalls.example

```html
<!DOCTYPE html>
<html lang="en">
<head>
<meta charset="utf-8">
<title>KWI Business Card</title>
<link rel="stylesheet" href="https://fonts.googleapis.com/css2?family=Red+Hat+Display:wght@400;700;800&display=swap">
<style>
  :root {
    --backdrop: #e4e4e4;
    --card-blue-top: #1ba0d8;
    --card-blue-bottom: #1c6fb8;
    --card-white: #f4f4f4;
    --brand-blue: #2f6db5;
    --text-light: #ffffff;
  }
  * { margin: 0; padding: 0; box-sizing: border-box; }
  html, body {
    width: 1200px; height: 960px; overflow: hidden;
    background: var(--backdrop);
    font-family: "Red Hat Display", Arial, sans-serif;
  }
  .canvas { position: relative; width: 1200px; height: 960px; }
  .card { position: absolute; left: 304px; width: 588px; height: 336px; overflow: hidden; }
  .card-front {
    top: 119px;
    background: linear-gradient(180deg, var(--card-blue-top) 0%, var(--card-blue-top) 40%, var(--card-blue-bottom) 100%);
    display: flex; align-items: center; justify-content: center;
  }
  .card-back { top: 506px; display: flex; }
  .brand-name {
    font-weight: 800; text-align: center; line-height: 1.05; letter-spacing: 0.04em;
  }
  .card-front .brand-name { color: var(--text-light); }
  .brand-initials { display: block; font-size: 86px; }
  .brand-full { display: block; font-size: 30px; margin-top: 8px; }
  .back-brand {
    width: 294px; height: 100%; background: var(--card-white);
    display: flex; align-items: center; justify-content: center;
  }
  .back-brand .brand-name { color: var(--brand-blue); }
  .back-brand .brand-initials { font-size: 58px; }
  .back-brand .brand-full { font-size: 20px; margin-top: 6px; }
  .back-details {
    flex: 1;
    background: linear-gradient(180deg, var(--card-blue-top) 0%, var(--card-blue-bottom) 100%);
    color: var(--text-light);
    padding: 82px 0 0 40px;
  }
  .person-name { font-size: 20px; font-weight: 700; letter-spacing: 0.03em; text-transform: uppercase; }
  .address { margin-top: 34px; font-size: 15px; line-height: 20px; font-weight: 400; }
  .contact-list { list-style: none; margin-top: 12px; font-size: 15px; line-height: 20px; }
  .contact-list li { display: flex; align-items: center; gap: 5px; white-space: nowrap; }
  .contact-icon { width: 13px; height: 13px; flex: none; }
</style>
</head>
<body>
<div class="canvas">
  <section class="card card-front">
    <div class="brand-name">
      <span class="brand-initials">KWI</span>
      <span class="brand-full">Korvel Walls, Inc.</span>
    </div>
  </section>

  <section class="card card-back">
    <div class="back-brand">
      <div class="brand-name">
        <span class="brand-initials">KWI</span>
        <span class="brand-full">Korvel Walls, Inc.</span>
      </div>
    </div>
    <div class="back-details">
      <h1 class="person-name">Dana Whitcombe</h1>
      <p class="address">218 Larkmoor Ave<br>Brenwick, OH 60418</p>
      <ul class="contact-list">
        <li>
          <svg class="contact-icon" viewBox="0 0 13 13" aria-hidden="true"><rect x="3" y="0.5" width="7" height="12" rx="1.3" fill="none" stroke="#fff" stroke-width="1.2"/><circle cx="6.5" cy="10.3" r="0.8" fill="#fff"/></svg>
          312-555-0178
        </li>
        <li>
          <svg class="contact-icon" viewBox="0 0 13 13" aria-hidden="true"><rect x="0.6" y="2.5" width="11.8" height="8" fill="none" stroke="#fff" stroke-width="1.2"/><path d="M0.6 2.5 L6.5 7 L12.4 2.5" fill="none" stroke="#fff" stroke-width="1.2"/></svg>
          dwhitcombe@korvelwalls.example
        </li>
        <li>
          <svg class="contact-icon" viewBox="0 0 13 13" aria-hidden="true"><circle cx="6.5" cy="6.5" r="5.8" fill="none" stroke="#fff" stroke-width="1.1"/><ellipse cx="6.5" cy="6.5" rx="2.5" ry="5.8" fill="none" stroke="#fff" stroke-width="1"/><path d="M0.7 6.5 H12.3" stroke="#fff" stroke-width="1"/></svg>
          www.korvelwalls.example
        </li>
      </ul>
    </div>
  </section>
</div>
</body>
</html>
```